Vehicle Rental Hire in the Algarve - Portugal

We are opening a Vehicle Rental company in the Algarve - Portugal - this will attract both locals and Tourists visiting. So we want this website to capture the beautiful location we will be set in, along with the familiarity of a vehicle rental company. And to keep a colour scheme in Line with out Logo. We are Marlenic Vehicle Rental.

Industry/Entity Type

Vehicle Rental

Number of Pages Required

1 page

Requirements
Must have
• must be professional, and simple to use navigation bar - must also have a "make a reservation" box - similar to the screenshot attached - Under our logo it must read "Vehicle Rental"
Nice to have
• It needs to be in a colour scheme that fits in with our logo

```html
<!DOCTYPE html>
<html lang="en">
<head>
<meta charset="utf-8">
<title>Marlenic Vehicle Rental</title>
<link rel="stylesheet" href="https://fonts.googleapis.com/css2?family=Outfit:wght@300;400;500;600;700&family=Caveat:wght@400&display=swap">
<style>
:root{
  --red:#d5262c;
  --navy:#0c0838;
  --ink:#14103f;
  --muted:#6d6b80;
  --soft:#f6f6fb;
  --card:#f4f4f8;
  --line:#dcdce6;
  --blue:#1b14c9;
  --white:#ffffff;
}
*{box-sizing:border-box;margin:0;padding:0}
html,body{width:1200px;height:4550px;overflow:hidden}
body{position:relative;font-family:"Outfit",sans-serif;color:var(--ink);background:var(--white)}
.abs{position:absolute}
a{color:inherit;text-decoration:none}
.btn{position:absolute;background:var(--red);color:var(--white);border-radius:4px;font-size:11px;display:flex;align-items:center;justify-content:center}

/* hero */
.hero{position:absolute;left:0;top:0;width:1200px;height:696px;overflow:hidden}
.hero-photo{position:absolute;inset:0;background:
  radial-gradient(ellipse at 75% 40%,#b79a72 0%,rgba(150,120,80,.6) 30%,transparent 60%),
  linear-gradient(180deg,#1d3a48 0%,#27464d 30%,#5a5d47 55%,#3c3a2c 80%,#2a2a22 100%)}
.hero-shade{position:absolute;inset:0;background:linear-gradient(90deg,rgba(10,20,30,.55),rgba(10,20,30,0) 60%)}
.brand{position:absolute;color:var(--white);text-align:center}
.brand-name{font-size:20px;font-weight:500;letter-spacing:.5px;line-height:1}
.brand-tag{font-size:9px;font-weight:300;letter-spacing:1.5px;margin-top:4px}
.nav{position:absolute;top:47px;left:442px;display:flex;gap:37px;font-size:12px;color:var(--white)}
.login{position:absolute;left:876px;top:47px;font-size:12px;color:var(--white)}
.hero-title{position:absolute;left:172px;top:196px;font-size:46px;font-weight:400;line-height:58px;color:var(--white)}
.hero-sub{position:absolute;left:172px;top:330px;font-family:"Caveat",cursive;font-size:30px;color:var(--white)}
.booking{position:absolute;left:172px;top:490px;width:854px;height:115px;background:rgba(255,255,255,.93);border-radius:10px}
.field-label{position:absolute;top:27px;font-size:11px;color:var(--ink)}
.field{position:absolute;top:50px;height:38px;border:1px solid var(--line);border-radius:4px;background:var(--white);font-size:10px;color:#9a98aa;display:flex;align-items:center;padding-left:10px;gap:6px;white-space:nowrap;overflow:hidden}
.field .sep{width:1px;height:16px;background:var(--line);margin:0 6px}

/* section headings */
.h2{position:absolute;font-size:28px;font-weight:600;color:var(--ink)}
.sub{position:absolute;font-size:11px;color:var(--muted)}

/* cars */
.car{position:absolute;width:270px}
.car-photo{height:230px;border-radius:8px;background:linear-gradient(180deg,#f7f7fa,#ececf2)}
.car-name{margin-top:20px;display:flex;justify-content:space-between;font-size:13px;font-weight:500}
.car-name span{font-size:11px;font-weight:400;color:var(--muted)}
.star{color:#f2b31c}
.car-spec{font-size:10.5px;color:var(--muted);margin-top:3px}
.car-seat{font-size:9.5px;color:var(--muted);margin-top:9px;display:flex;gap:40px}
.car-price{margin-top:22px;border-top:1px solid var(--line);padding-top:12px;display:flex;justify-content:space-between;align-items:center;font-size:10px;color:var(--muted)}
.car-price b{font-size:14px;color:var(--ink);font-weight:600}

/* about */
.about{position:absolute;left:0;top:1775px;width:1200px;height:575px;background:var(--soft)}
.about-text{position:absolute;left:172px;top:242px;width:345px;font-size:11px;line-height:21px;color:var(--muted)}
.ring{position:absolute;border-radius:50%}

/* why */
.feature{position:absolute;display:block;width:200px;max-width:200px;text-align:center}
.feature-icon{width:76px;height:76px;margin:0 auto;border-radius:50%;background:var(--white);box-shadow:0 6px 18px rgba(30,30,80,.09);display:flex;align-items:center;justify-content:center}
.feature-title{display:block;width:200px;font-size:16px;font-weight:500;margin-top:32px;white-space:nowrap}
.feature-text{display:block;width:200px;max-width:200px;margin:28px 0 0 0;font-size:10.5px;line-height:21px;color:var(--muted);white-space:normal;overflow-wrap:break-word}
.band{position:absolute;left:0;top:2740px;width:1200px;height:318px;background:linear-gradient(180deg,#ffffff 0%,#e4e9f1 25%,#cfd8e3 60%,#9fb279 88%,#4f7a2c 100%)}
.band-word{position:absolute;left:420px;top:2830px;font-size:68px;font-weight:600;color:rgba(255,255,255,.35);letter-spacing:2px}

/* testimonials */
.review{position:absolute;width:270px}
.review-photo{height:150px;border-radius:4px}
.review h4{font-size:13px;font-weight:500;margin-top:32px}
.review p{width:270px;font-size:10.5px;line-height:21px;color:var(--muted);margin-top:10px}
.review .who{font-size:10.5px;font-weight:600;margin-top:16px}
.review .where{font-size:9px;color:var(--muted);margin-top:2px}
.quote{position:absolute;right:20px;bottom:2px;font-size:54px;line-height:1;color:#cfd0ee;font-weight:700}
.arrow{position:absolute;width:38px;height:38px;border-radius:50%;display:flex;align-items:center;justify-content:center}

/* faq */
.faq{position:absolute;left:0;top:3555px;width:1200px;height:615px;background:var(--soft)}
.faq-item{position:absolute;left:245px;width:710px;font-size:13px;font-weight:500;display:flex;justify-content:space-between;align-items:center}
.faq-answer{position:absolute;left:245px;width:680px;font-size:10.5px;line-height:21px;color:var(--muted)}
.faq-line{position:absolute;left:245px;width:710px;height:1px;background:var(--line)}

/* footer */
.footer{position:absolute;left:0;top:4170px;width:1200px;height:380px;background:var(--navy);color:#c9c7dd}
.footer h5{position:absolute;font-size:12px;font-weight:500;color:var(--white)}
.footer ul{position:absolute;list-style:none;font-size:11px;line-height:32px}
.footer .about-f{position:absolute;left:172px;top:175px;width:220px;font-size:11px;line-height:21px}
.sub-input{position:absolute;left:777px;top:120px;width:160px;height:36px;border:1px solid #2e2a62;border-radius:4px 0 0 4px;font-size:11px;display:flex;align-items:center;padding-left:14px;color:#9795b5}
.copy{position:absolute;left:0;width:1200px;top:325px;text-align:center;font-size:11px}
</style>
</head>
<body>

<header class="hero">
  <div class="hero-photo" role="img" aria-label="Aerial photo of a winding coastal road with a car, rocky hillside and river in the Algarve"></div>
  <div class="hero-shade"></div>
  <div class="brand" style="left:168px;top:38px">
    <div class="brand-name">Marlenic</div>
    <div class="brand-tag">Vehicle Rental</div>
  </div>
  <nav class="nav">
    <a href="#">Home</a><a href="#">Our Cars</a><a href="#">About Us</a><a href="#">Contact Us</a>
  </nav>
  <a class="login" href="#">Login</a>
  <a class="btn" href="#" style="left:938px;top:37px;width:88px;height:35px;font-size:12px">Sign Up</a>
  <h1 class="hero-title">Hassle Free Car<br>Rental in Portagal</h1>
  <div class="hero-sub">Take a Rent for Your Every Journey</div>

  <form class="booking">
    <div class="field-label" style="left:28px">Collect From</div>
    <div class="field-label" style="left:195px">Drop To</div>
    <div class="field-label" style="left:363px">Collect Date &amp; Time</div>
    <div class="field-label" style="left:557px">Drop Date &amp; Time</div>
    <div class="field" style="left:28px;width:160px">
      <svg width="11" height="13" viewBox="0 0 11 13"><path d="M5.5 12s4-4.2 4-7a4 4 0 0 0-8 0c0 2.8 4 7 4 7z" fill="none" stroke="#9a98aa"/><circle cx="5.5" cy="5" r="1.4" fill="none" stroke="#9a98aa"/></svg>City, Location</div>
    <div class="field" style="left:195px;width:160px">
      <svg width="11" height="13" viewBox="0 0 11 13"><path d="M5.5 12s4-4.2 4-7a4 4 0 0 0-8 0c0 2.8 4 7 4 7z" fill="none" stroke="#9a98aa"/><circle cx="5.5" cy="5" r="1.4" fill="none" stroke="#9a98aa"/></svg>City, Location</div>
    <div class="field" style="left:363px;width:186px">
      <svg width="11" height="13" viewBox="0 0 11 13"><path d="M5.5 12s4-4.2 4-7a4 4 0 0 0-8 0c0 2.8 4 7 4 7z" fill="none" stroke="#9a98aa"/><circle cx="5.5" cy="5" r="1.4" fill="none" stroke="#9a98aa"/></svg>14 Apr, 2024<span class="sep"></span>10:30 AM
      <svg width="8" height="6" viewBox="0 0 8 6"><path d="M1 1l3 3 3-3" fill="none" stroke="#9a98aa"/></svg></div>
    <div class="field" style="left:557px;width:186px">
      <svg width="11" height="13" viewBox="0 0 11 13"><path d="M5.5 12s4-4.2 4-7a4 4 0 0 0-8 0c0 2.8 4 7 4 7z" fill="none" stroke="#9a98aa"/><circle cx="5.5" cy="5" r="1.4" fill="none" stroke="#9a98aa"/></svg>14 Apr, 2024<span class="sep"></span>10:30 AM
      <svg width="8" height="6" viewBox="0 0 8 6"><path d="M1 1l3 3 3-3" fill="none" stroke="#9a98aa"/></svg></div>
    <div class="btn" style="left:751px;top:50px;width:76px;height:38px">Go</div>
  </form>
</header>

<section>
  <h2 class="h2" style="left:172px;top:770px">Top Picks Vehicle This Month</h2>
  <p class="sub" style="left:172px;top:815px">It is a long established fact that a reader will be distracted by the readable content of a page</p>

  <article class="car" style="left:172px;top:866px">
    <div class="car-photo" role="img" aria-label="Bronze hatchback car"></div>
    <div class="car-name">Veltra <span><b class="star">★</b> 4.7</span></div>
    <div class="car-spec">Automatic / Manual</div>
    <div class="car-seat"><span>Seat: 4</span><span>Airbag: 1</span></div>
    <div class="car-price">Start From <b>€70/ Day</b></div>
  </article>
  <article class="car" style="left:464px;top:866px">
    <div class="car-photo" role="img" aria-label="Black sports coupe"></div>
    <div class="car-name">Veltra <span><b class="star">★</b> 4.7</span></div>
    <div class="car-spec">Automatic / Manual</div>
    <div class="car-seat"><span>Seat: 4</span><span>Airbag: 1</span></div>
    <div class="car-price">Start From <b>€70/ Day</b></div>
  </article>
  <article class="car" style="left:756px;top:866px">
    <div class="car-photo" role="img" aria-label="Black pickup truck"></div>
    <div class="car-name">Veltra <span><b class="star">★</b> 4.7</span></div>
    <div class="car-spec">Automatic / Manual</div>
    <div class="car-seat"><span>Seat: 4</span><span>Airbag: 1</span></div>
    <div class="car-price">Start From <b>€70/ Day</b></div>
  </article>
  <article class="car" style="left:172px;top:1264px">
    <div class="car-photo" role="img" aria-label="Red classic muscle car with white stripes"></div>
    <div class="car-name">Veltra <span><b class="star">★</b> 4.7</span></div>
    <div class="car-spec">Automatic / Manual</div>
    <div class="car-seat"><span>Seat: 4</span><span>Airbag: 1</span></div>
    <div class="car-price">Start From <b>€70/ Day</b></div>
  </article>
  <article class="car" style="left:464px;top:1264px">
    <div class="car-photo" role="img" aria-label="White SUV"></div>
    <div class="car-name">Veltra <span><b class="star">★</b> 4.7</span></div>
    <div class="car-spec">Automatic / Manual</div>
    <div class="car-seat"><span>Seat: 4</span><span>Airbag: 1</span></div>
    <div class="car-price">Start From <b>€70/ Day</b></div>
  </article>
  <article class="car" style="left:756px;top:1264px">
    <div class="car-photo" role="img" aria-label="Blue classic convertible"></div>
    <div class="car-name">Veltra <span><b class="star">★</b> 4.7</span></div>
    <div class="car-spec">Automatic / Manual</div>
    <div class="car-seat"><span>Seat: 4</span><span>Airbag: 1</span></div>
    <div class="car-price">Start From <b>€70/ Day</b></div>
  </article>
  <a class="btn" href="#" style="left:538px;top:1677px;width:124px;height:37px">View All</a>
</section>

<section class="about">
  <h2 class="h2" style="left:172px;top:135px;line-height:37px;font-size:29px">Vehicle Rental company<br>in the Algarve - Portugal</h2>
  <p class="about-text">Lorem Ipsum is simply dummy text of the printing and typesetting industry. Lorem Ipsum has been the industry's standard dummy text ever since the 1500s, when an unknown printer took a galley of type and scrambled it to make a type specimen book. It has survived not only five centuries, but also the leap into electronic typesetting, remaining</p>
  <a class="btn" href="#" style="left:172px;top:397px;width:124px;height:37px">Learn More</a>
  <svg class="abs" style="left:600px;top:70px" width="430" height="430" viewBox="0 0 430 430">
    <path d="M60 120 A185 185 0 0 1 340 60" fill="none" stroke="#d9d8ec" stroke-width="2"/>
    <path d="M395 150 A190 190 0 0 1 310 380" fill="none" stroke="#d9d8ec" stroke-width="2"/>
    <path d="M40 260 A185 185 0 0 0 150 395" fill="none" stroke="#d9d8ec" stroke-width="2"/>
    <circle cx="215" cy="215" r="182" fill="#ffffff" opacity=".7"/>
    <circle cx="215" cy="215" r="172" fill="none" stroke="#c9c6ee" stroke-width="6" opacity=".6"/>
  </svg>
  <div class="ring" role="img" aria-label="Happy family with a dog leaning out of a car window" style="left:650px;top:120px;width:330px;height:330px;background:radial-gradient(circle at 50% 40%,#e9d7c6,#8bb2c9 55%,#4d7f6c 100%)"></div>
</section>

<section>
  <h2 class="h2" style="left:0;width:1200px;text-align:center;top:2423px">Why You Choose Us</h2>
  <p class="sub" style="left:0;width:1200px;text-align:center;top:2470px">It is a long established fact that a reader will be distracted by the readable</p>

  <div class="feature" style="left:170px;top:2527px;width:200px">
    <div class="feature-icon"><svg width="22" height="24" viewBox="0 0 22 24"><circle cx="11" cy="8" r="8" fill="var(--blue)"/><text x="11" y="12" text-anchor="middle" font-size="11" fill="#fff" font-family="Outfit">$</text><path d="M5 19l6 4 6-4" fill="none" stroke="var(--blue)" stroke-width="2.5"/></svg></div>
    <div class="feature-title">Low Pricing</div>
    <div class="feature-text" style="width:200px">Lorem Ipsum is simply dummy text of the printing and typesetting industry rem Ipsum has</div>
  </div>
  <div class="feature" style="left:390px;top:2527px;width:200px">
    <div class="feature-icon"><svg width="28" height="24" viewBox="0 0 28 24"><circle cx="14" cy="12" r="8" fill="none" stroke="var(--blue)" stroke-width="2.5"/><path d="M14 8l1.3 2.6 2.8.4-2 2 .5 2.8-2.6-1.4-2.6 1.4.5-2.8-2-2 2.8-.4z" fill="var(--blue)"/><path d="M4 6c-3 4-3 8 0 12M24 6c3 4 3 8 0 12" fill="none" stroke="var(--blue)" stroke-width="2"/></svg></div>
    <div class="feature-title">High Quality</div>
    <div class="feature-text" style="width:200px">Lorem Ipsum is simply dummy text of the printing and typesetting industry rem Ipsum has</div>
  </div>
  <div class="feature" style="left:609px;top:2527px;width:200px">
    <div class="feature-icon"><svg width="22" height="24" viewBox="0 0 22 24"><path d="M11 1l9 3.5v7c0 5.5-4 9.5-9 11.5-5-2-9-6-9-11.5v-7z" fill="var(--blue)"/><path d="M7 12l3 3 5-6" fill="none" stroke="#fff" stroke-width="2"/></svg></div>
    <div class="feature-title">Clean &amp; Safe</div>
    <div class="feature-text" style="width:200px">Lorem Ipsum is simply dummy text of the printing and typesetting industry rem Ipsum has</div>
  </div>
  <div class="feature" style="left:828px;top:2527px;width:200px">
    <div class="feature-icon"><svg width="26" height="26" viewBox="0 0 26 26"><path d="M13 1l3 2.5 4-.5 1 3.8 3.5 2-1.5 3.7 1.5 3.7-3.5 2-1 3.8-4-.5-3 2.5-3-2.5-4 .5-1-3.8-3.5-2 1.5-3.7-1.5-3.7 3.5-2 1-3.8 4 .5z" fill="var(--blue)"/><text x="13" y="17" text-anchor="middle" font-size="10" fill="#fff" font-family="Outfit">%</text></svg></div>
    <div class="feature-title">Best Discounts</div>
    <div class="feature-text" style="width:200px">Lorem Ipsum is simply dummy text of the printing and typesetting industry rem Ipsum has</div>
  </div>

  <div class="band" role="img" aria-label="White SUV parked on grass beside a family walking together under a soft sky"></div>
  <div class="band-word">MARLENIC</div>
</section>

<section>
  <h2 class="h2" style="left:172px;top:3168px;font-size:29px;line-height:37px">What Our<br>Customer Say<br>About Us</h2>
  <p class="sub" style="left:172px;top:3305px;width:190px;line-height:21px;font-size:10.5px">It is a long established fact that a reader will be distracted by the readable</p>
  <div class="arrow" style="left:174px;top:3401px;background:#e7e7ee"><svg width="14" height="10" viewBox="0 0 14 10"><path d="M13 5H2M6 1L2 5l4 4" fill="none" stroke="var(--ink)" stroke-width="1.5"/></svg></div>
  <div class="arrow" style="left:221px;top:3401px;background:#e7e7ee"><svg width="14" height="10" viewBox="0 0 14 10"><path d="M1 5h11M8 1l4 4-4 4" fill="none" stroke="var(--ink)" stroke-width="1.5"/></svg></div>

  <article class="review" style="left:450px;top:3136px">
    <div class="review-photo" role="img" aria-label="Two friends laughing in a blue convertible among trees" style="background:linear-gradient(160deg,#d8a867,#5b8fb2 55%,#2f6a9a)"></div>
    <h4>Very simple to rent the car</h4>
    <p>Lorem Ipsum is simply dummy text of the printing and typesetting industry. Lorem Ipsum has been the industry's standard dummy text ever since the 1500s</p>
    <div class="who">Tomas Varela</div>
    <div class="where">Algarve - Portugal</div>
    <div class="quote">”</div>
  </article>
  <article class="review" style="left:757px;top:3136px">
    <div class="review-photo" role="img" aria-label="Couple smiling in a white convertible on a sunny road" style="background:linear-gradient(160deg,#e8eef2,#a9b8c2 50%,#6d7f86)"></div>
    <h4>Very simple to rent the car</h4>
    <p>Lorem Ipsum is simply dummy text of the printing and typesetting industry. Lorem Ipsum has been the industry's standard dummy text ever since the 1500s</p>
    <div class="who">Tomas Varela</div>
    <div class="where">Algarve - Portugal</div>
    <div class="quote">”</div>
  </article>
</section>

<section class="faq">
  <h2 class="h2" style="left:0;width:1200px;text-align:center;top:64px">Frequently Asked Questions</h2>
  <p class="sub" style="left:0;width:1200px;text-align:center;top:110px">It is a long established fact that a reader will be distracted by the readable</p>

  <div class="faq-item" style="top:162px">Lorem Ipsum is simply dummy text of the printing?
    <svg width="18" height="18" viewBox="0 0 18 18"><circle cx="9" cy="9" r="8" fill="none" stroke="var(--ink)"/><path d="M5.5 10.5L9 7l3.5 3.5" fill="none" stroke="var(--ink)"/></svg></div>
  <p class="faq-answer" style="top:192px">Lorem Ipsum is simply dummy text of the printing and typesetting industry. Lorem Ipsum has been the industry's standard dummy text ever since the 1500s, when an unknown printer took a galley of type and scrambled it to make a type specimen book.</p>
  <div class="faq-line" style="top:283px"></div>

  <div class="faq-item" style="top:306px">It is a long established fact that a reader will be distracted?
    <svg width="18" height="18" viewBox="0 0 18 18"><circle cx="9" cy="9" r="8" fill="none" stroke="var(--ink)"/><path d="M5.5 7.5L9 11l3.5-3.5" fill="none" stroke="var(--ink)"/></svg></div>
  <div class="faq-line" style="top:351px"></div>

  <div class="faq-item" style="top:375px">Many desktop publishing packages and web page?
    <svg width="18" height="18" viewBox="0 0 18 18"><circle cx="9" cy="9" r="8" fill="none" stroke="var(--ink)"/><path d="M5.5 7.5L9 11l3.5-3.5" fill="none" stroke="var(--ink)"/></svg></div>
  <div class="faq-line" style="top:420px"></div>

  <div class="faq-item" style="top:444px">There are many variations of passages of Lorem Ipsum available?
    <svg width="18" height="18" viewBox="0 0 18 18"><circle cx="9" cy="9" r="8" fill="none" stroke="var(--ink)"/><path d="M5.5 7.5L9 11l3.5-3.5" fill="none" stroke="var(--ink)"/></svg></div>
  <div class="faq-line" style="top:489px"></div>

  <div class="faq-item" style="top:513px">The standard chunk of Lorem Ipsum used since the 1500s is reproduced below for those?
    <svg width="18" height="18" viewBox="0 0 18 18"><circle cx="9" cy="9" r="8" fill="none" stroke="var(--ink)"/><path d="M5.5 7.5L9 11l3.5-3.5" fill="none" stroke="var(--ink)"/></svg></div>
</section>

<footer class="footer">
  <div class="brand" style="left:172px;top:105px;color:#6f6cf0">
    <div class="brand-name">Marlenic</div>
    <div class="brand-tag">Vehicle Rental</div>
  </div>
  <p class="about-f">Lorem Ipsum is simply dummy text of the printing and typesetting industry.</p>

  <h5 style="left:465px;top:78px">Quick Links</h5>
  <ul style="left:465px;top:110px"><li>Home</li><li>Our Cars</li><li>About Us</li><li>Contact Us</li></ul>
  <h5 style="left:611px;top:78px">Support</h5>
  <ul style="left:611px;top:110px"><li>Contac Us</li><li>Faq's</li><li>Terms &amp; Condition</li></ul>
  <h5 style="left:777px;top:78px">Get Updates</h5>
  <div class="sub-input">Enter Your Email</div>
  <div class="btn" style="left:937px;top:120px;width:89px;height:36px;font-size:11px">Subscribe</div>
  <div class="copy">Copyright © 2024 Marlenic. All Rights Reserved</div>
</footer>

</body>
</html>
```